International Consulting Firm
Stationery incl. business cards, letterhead, envelope, PPT template, and brochure
Professional
DMN QRT
CHIEF EXECUTIVE OFFICER
LEVEL 4,
7 MOOR LANE
FERN HOUSE
GOTHAM CITY
DMN@DORSETTPRYCE.EXAMPLE
WWW.DORSETTPRYCE.EXAMPLE
The fonts used in the logo are (a) Eras Bold ITC & (b)BankGothic
Logo only
This fantastic logo was designed recently by quarbin and we now need stationery to support it.

```html
<!DOCTYPE html>
<html lang="en">
<head>
<meta charset="utf-8">
<title>Dorsett Pryce — Business Cards</title>
<link href="https://fonts.googleapis.com/css2?family=Montserrat:wght@400;600;700&display=swap" rel="stylesheet">
<style>
  :root {
    --backdrop: #4a2a1d;
    --card-black: #0d0d0d;
    --card-white: #f4f4f4;
    --ink-light: #ffffff;
    --ink-muted: #bdbdbd;
    --ink-dark: #111111;
  }
  html, body {
    margin: 0;
    padding: 0;
    width: 1200px;
    height: 897px;
    overflow: hidden;
    background: var(--backdrop);
    font-family: "Montserrat", Arial, sans-serif;
  }
  .stage {
    position: relative;
    width: 1200px;
    height: 897px;
    display: flex;
    align-items: center;
    justify-content: center;
    gap: 50px;
  }
  .card {
    position: relative;
    width: 540px;
    height: 310px;
    border-radius: 18px;
    background: var(--card-black);
    overflow: hidden;
    box-shadow: 0 10px 24px rgba(0,0,0,0.45);
  }
  .card-front .white-field {
    position: absolute;
    left: 0;
    top: 0;
    width: 540px;
    height: 310px;
  }
  .brand {
    position: absolute;
    display: flex;
    align-items: center;
    gap: 10px;
    font-weight: 700;
    letter-spacing: 1.5px;
    white-space: nowrap;
  }
  .brand-dot {
    border-radius: 50%;
    flex: none;
  }
  .card-front .brand {
    left: 28px;
    top: 170px;
    color: var(--ink-dark);
    font-size: 19px;
  }
  .card-front .brand-dot {
    width: 20px;
    height: 20px;
    background: var(--ink-dark);
  }
  .contact {
    position: absolute;
    right: 30px;
    top: 30px;
    text-align: right;
    color: var(--ink-light);
    text-transform: uppercase;
  }
  .contact .name {
    font-size: 17px;
    font-weight: 700;
    letter-spacing: 1px;
    margin: 0;
  }
  .contact .role {
    font-size: 10px;
    font-weight: 600;
    letter-spacing: 1.2px;
    color: var(--ink-muted);
    margin: 4px 0 16px;
  }
  .contact .lines {
    font-size: 9.5px;
    line-height: 15px;
    letter-spacing: 0.8px;
    margin: 0;
  }
  .contact .email {
    font-size: 9.5px;
    letter-spacing: 0.8px;
    margin: 14px 0 0;
    font-weight: 600;
  }
  .card-back {
    display: flex;
    flex-direction: column;
    align-items: center;
    justify-content: center;
    gap: 18px;
  }
  .card-back .brand {
    position: static;
    color: var(--ink-light);
    font-size: 24px;
  }
  .card-back .brand-dot {
    width: 24px;
    height: 24px;
    background: var(--ink-light);
  }
  .web {
    color: var(--ink-light);
    font-size: 11px;
    letter-spacing: 2px;
    font-weight: 600;
  }
</style>
</head>
<body>
  <main class="stage">
    <section class="card card-front">
      <svg class="white-field" viewBox="0 0 540 310" aria-hidden="true">
        <path d="M0 70 C 80 60, 170 55, 225 105 C 270 150, 250 230, 285 310 L0 310 Z" fill="var(--card-white)"/>
      </svg>
      <div class="brand"><span class="brand-dot"></span>DORSETT PRYCE</div>
      <div class="contact">
        <p class="name">DMN QRT</p>
        <p class="role">Chief Executive Officer</p>
        <p class="lines">
          Level 4,<br>
          7 Moor Lane<br>
          Fern House<br>
          Gotham City<br>
          T 000 555 0101<br>
          F 000 555 0102<br>
          M 000 555 0103
        </p>
        <p class="email">DMN@DORSETTPRYCE.EXAMPLE</p>
      </div>
    </section>
    <section class="card card-back">
      <div class="brand"><span class="brand-dot"></span>DORSETT PRYCE</div>
      <div class="web">WWW.DORSETTPRYCE.EXAMPLE</div>
    </section>
  </main>
</body>
</html>
```